Banner for real estate email blast

I need a banner created that will be used in a commercial real estate broadcast email headed. The banner size should be 800x129 pixels and in a JPG format. I will include our company logo and samples of some other company documents.
The banner MUST include (1) the company name, Holloway-Brisk Real Estate and (2) the following contact information:
472 Tindale Orchard Rd
Fayetteville, NC 28417
(910) 463-2058
www.HollowayBriskRE.example
Target Market(s)
Real estate agents.
Industry/Entity Type
Real Estate
Requirements
Must have
- 1. Company name
- 2. Contact info to include address, phone number, web address
- 3. Use the same green colors as in our other attached documents.
- 4. MUST be 800x129 pixels
Should not have
- Any other text other than what is mentioned in the "Must Haves"

```html
<!DOCTYPE html>
<html lang="en">
<head>
<meta charset="utf-8">
<title>Holloway-Brisk Real Estate – Email Banner</title>
<link rel="stylesheet" href="https://fonts.googleapis.com/css2?family=EB+Garamond:wght@400&display=swap">
<style>
  :root {
    --brand-green: #036d06;
    --leaf-green: #2f8a31;
    --paper: #ffffff;
    --backdrop: #e9ecef;
  }
  html, body {
    margin: 0;
    padding: 0;
    width: 1200px;
    height: 800px;
    overflow: hidden;
    background: var(--backdrop);
  }
  .canvas {
    position: relative;
    width: 1200px;
    height: 800px;
  }
  .banner {
    position: absolute;
    left: 0;
    top: 280px;
    width: 1200px;
    height: 241px;
    background: var(--paper);
    overflow: hidden;
    font-family: "EB Garamond", Garamond, serif;
  }
  .banner-shape {
    position: absolute;
    inset: 0;
  }
  .brand {
    position: absolute;
    left: 36px;
    top: 53px;
    display: flex;
    align-items: center;
    gap: 16px;
  }
  .brand-dot {
    width: 96px;
    height: 96px;
    border-radius: 50%;
    background: var(--brand-green);
    flex: none;
  }
  .brand-name {
    margin: 0;
    font-size: 38px;
    font-weight: 400;
    color: var(--brand-green);
    white-space: nowrap;
  }
  .contact {
    position: absolute;
    right: 34px;
    top: 44px;
    text-align: right;
    color: var(--paper);
    font-size: 24px;
    line-height: 36px;
    white-space: nowrap;
  }
  .contact p { margin: 0; }
  .contact-rule {
    border: 0;
    border-top: 1px solid var(--paper);
    margin: 6px 0 8px;
  }
</style>
</head>
<body>
<div class="canvas">
  <section class="banner">
    <svg class="banner-shape" width="1200" height="241" viewBox="0 0 1200 241" aria-hidden="true">
      <path fill="var(--brand-green)"
        d="M221,241 C260,214 330,204 420,226 C470,240 505,178 565,118 C625,50 685,10 745,0 L1200,0 L1200,241 Z"/>
    </svg>
    <svg class="banner-shape" width="1200" height="241" viewBox="0 0 1200 241" role="img" aria-label="Leafy vine ornament curling up along the edge of the green field">
      <defs>
        <linearGradient id="vine-fade" x1="0" y1="1" x2="1" y2="0">
          <stop offset="0" stop-color="var(--leaf-green)" stop-opacity="0.55"/>
          <stop offset="1" stop-color="var(--leaf-green)" stop-opacity="0.25"/>
        </linearGradient>
      </defs>
      <path fill="url(#vine-fade)"
        d="M500,232 C520,180 560,120 610,70 C660,25 720,4 790,6 C730,30 680,70 640,120 C600,170 560,215 520,240 Z"/>
    </svg>

    <div class="brand">
      <span class="brand-dot"></span>
      <h1 class="brand-name">Holloway-Brisk Real Estate</h1>
    </div>

    <div class="contact">
      <p class="contact-phone">(910) 463-2058</p>
      <p class="contact-web">www.HollowayBriskRE.example</p>
      <hr class="contact-rule">
      <p class="contact-street">472 Tindale Orchard Rd</p>
      <p class="contact-city">Fayetteville, NC 28417</p>
    </div>
  </section>
</div>
</body>
</html>
```